Email Marketing for Post-wren

I am a sports photographer and I would like to have an email distribution that I can send out after an event or have something go out on a more regular basis.

juniperridge-peakshot.com

I can supply the looks and so on I am looking for a template that I can reuse time and time again.

I want something that works with Postwren.

http://postwrenmail.com

It must conform to there templates and I would like to be able to put some photo's in the template as well.

Target Market(s)

Parents and Families attending events and wishing to purchase photos from that day.

Industry/Entity Type

Marketing

Font styles to use
Serif

Requirements
Must have
• Must have my logo.
• Must use the same font museo 500.
• Must be Red, Grey and White same as the logo.
• Must have Facebook links https://www.pallorium.net/JuniperRidgePeakshot
• Must have twitter links @junipeakshot
• Must have email address info@juniperridge-peakshot.com
• Must have room for other company logo's in the future
• Should be broken down in sections

```html
<!DOCTYPE html>
<html lang="en">
<head>
<meta charset="utf-8">
<title>Postwren Newsletter – Packages &amp; Scenery Photography</title>
<link rel="stylesheet" href="https://fonts.googleapis.com/css2?family=Arimo:wght@400;700&family=Open+Sans:wght@600;700&display=swap">
<style>
  :root {
    --brand-red: #e4161b;
    --text-dark: #3a3a3a;
    --text-mid: #555555;
    --page-grey: #cfcfcf;
    --rule-grey: #d9d9d9;
    --white: #ffffff;
  }
  * { box-sizing: border-box; margin: 0; padding: 0; }
  html, body { width: 779px; height: 1200px; overflow: hidden; }
  body {
    background: var(--page-grey);
    font-family: "Arimo", Arial, sans-serif;
    color: var(--text-dark);
  }
  .email {
    position: absolute;
    left: 57px; top: 0;
    width: 665px; height: 1200px;
    background: var(--white);
    padding: 26px 21px 0;
  }
  .section-bar {
    height: 52px;
    background: var(--brand-red);
    color: var(--white);
    font-weight: 700;
    font-size: 19px;
    letter-spacing: 0.5px;
    padding-left: 18px;
    display: flex;
    align-items: center;
  }
  .packages {
    display: grid;
    grid-template-columns: 317px 306px;
    row-gap: 34px;
    padding: 30px 0 0 16px;
  }
  .package-title {
    font-size: 19px;
    font-weight: 400;
    color: var(--text-dark);
    margin-bottom: 14px;
  }
  .package-features {
    list-style: disc;
    padding-left: 52px;
    font-size: 13px;
    line-height: 17px;
    color: var(--text-mid);
    min-height: 90px;
  }
  .package-features li { padding-left: 6px; }
  .package-price {
    color: var(--brand-red);
    font-size: 13px;
    margin: 16px 0 10px;
  }
  .btn {
    display: inline-block;
    background: var(--brand-red);
    color: var(--white);
    font-weight: 700;
    text-decoration: none;
    border-radius: 3px;
  }
  .btn-small {
    font-size: 10px;
    padding: 12px 10px;
    letter-spacing: 0.3px;
  }
  .divider {
    height: 2px;
    background: var(--rule-grey);
    margin: 38px 0 0;
  }
  .gallery-title {
    font-family: "Open Sans", Arial, sans-serif;
    font-weight: 600;
    color: var(--brand-red);
    font-size: 40px;
    text-align: center;
    margin-top: 20px;
    line-height: 52px;
  }
  .photo {
    border-radius: 2px;
  }
  .photo-wide {
    height: 112px;
    margin-top: 21px;
    background: linear-gradient(90deg, #6f6a66 0%, #b7c0c8 25%, #8c5a4e 45%, #c4c9cf 65%, #5e5b5a 85%, #a9b3bc 100%);
  }
  .photo-row {
    display: flex;
    justify-content: space-between;
    padding: 0 12px;
    margin-top: 18px;
  }
  .photo-half {
    width: 281px;
    height: 165px;
  }
  .photo-pier { background: linear-gradient(180deg, #bdbdbd 0%, #6a6a6a 55%, #1e1e1e 100%); }
  .photo-palms { background: linear-gradient(180deg, #e6e6e6 0%, #9a9a9a 60%, #3c3c3c 100%); }
  .gallery-text {
    text-align: center;
    font-size: 11px;
    color: var(--text-mid);
    margin-top: 32px;
  }
  .gallery-cta {
    text-align: center;
    margin-top: 13px;
  }
  .btn-large {
    width: 190px;
    height: 48px;
    line-height: 48px;
    font-size: 14px;
    text-align: center;
  }
  .divider-bottom { margin-top: 38px; }
</style>
</head>
<body>
<main class="email">
  <header class="section-bar">PACKAGES</header>

  <section class="packages">
    <article class="package">
      <h2 class="package-title">Package 1 - Bang For Buck!</h2>
      <ul class="package-features">
        <li>Your choice for location</li>
        <li>5 images (of your choice) available for download</li>
        <li>One A3 print</li>
        <li>Two 8 x 10 prints</li>
      </ul>
      <p class="package-price">$350</p>
      <a class="btn btn-small" href="#">BOOK NOW</a>
    </article>
    <article class="package">
      <h2 class="package-title">Package 2 - You Choose</h2>
      <ul class="package-features">
        <li>Your choice for location</li>
        <li>5 images (of your choice) available for download</li>
        <li>One A3 print</li>
        <li>Three 8 x 12 prints</li>
      </ul>
      <p class="package-price">$450</p>
      <a class="btn btn-small" href="#">BOOK NOW</a>
    </article>
    <article class="package">
      <h2 class="package-title">Package 3 - All-in-One</h2>
      <ul class="package-features">
        <li>Your choice for location</li>
        <li>10 images (of your choice) available for download</li>
        <li>Two A3 prints</li>
        <li>Three 8 x 12 prints</li>
      </ul>
      <p class="package-price">$600</p>
      <a class="btn btn-small" href="#">BOOK NOW</a>
    </article>
    <article class="package">
      <h2 class="package-title">Parties &amp; Social Events</h2>
      <ul class="package-features">
        <li>Up to 3 hours</li>
        <li>15 images (of your choice) available for download</li>
      </ul>
      <p class="package-price">$375</p>
      <a class="btn btn-small" href="#">BOOK NOW</a>
    </article>
  </section>

  <div class="divider"></div>

  <section class="gallery">
    <h2 class="gallery-title">Scenery Photography</h2>
    <div class="photo photo-wide" role="img" aria-label="Wide photo of a busy city square with colourful billboards"></div>
    <div class="photo-row">
      <div class="photo photo-half photo-pier" role="img" aria-label="Black and white photo of a long pier stretching over the sea"></div>
      <div class="photo photo-half photo-palms" role="img" aria-label="Black and white photo of palm trees on a beach"></div>
    </div>
    <p class="gallery-text">In the mood for some landscapes? We've got plenty to choose from on our website. Check it out!</p>
    <div class="gallery-cta">
      <a class="btn btn-large" href="#">Click Here to see more!</a>
    </div>
  </section>

  <div class="divider divider-bottom"></div>
</main>
</body>
</html>
```